Business Card for Ferncliff Massage

I need a business card for my massage therapy & cannabis oil practice. I already have a logo,the "massage" got edited out of this file. I will send the original soon. I need these elements to be on the card:
web: FerncliffMassage.example
ph: 417/283-9061
email: Mirela.Dawkant@mailbox.example
Other slogans, statements to consider:
Science Geek, Massage Therapist, Neuromuscular Therapy, Cannabis Spa Treatments, Raindrop Therapy, Essential Oils
Target Market(s)
women between 20 & 65, people with enough $ to afford regular massage, people who recently had a motor vehicle accident, Halvora HMP insured
Industry/Entity Type
Massage Therapy
Contact Information for Business Card
I would like to see my bear logo featured; contact details, greens & blues preferred colors.

```html
<!DOCTYPE html>
<html lang="en">
<head>
<meta charset="utf-8">
<title>Ferncliff Massage – Business Card</title>
<link href="https://fonts.googleapis.com/css2?family=Roboto:wght@300;400;500;700&display=swap" rel="stylesheet">
<style>
  :root {
    --backdrop: #5a5a5a;
    --brown: #726356;
    --green: #2f7d3e;
    --white: #ffffff;
  }
  * { box-sizing: border-box; margin: 0; padding: 0; }
  html, body { width: 1200px; height: 1200px; overflow: hidden; }
  body {
    background: var(--backdrop);
    font-family: "Roboto", Arial, sans-serif;
    position: relative;
  }
  .card {
    position: absolute;
    left: 270px;
    width: 660px;
    height: 374px;
    border-radius: 16px;
    overflow: hidden;
    box-shadow: 0 6px 14px rgba(0,0,0,0.45);
  }
  .card--front { top: 196px; background: var(--brown); }
  .card--back { top: 630px; background: var(--green); }

  .front-shape { position: absolute; inset: 0; }

  .brand {
    position: absolute;
    left: 40px; top: 170px;
    width: 200px;
    display: flex; align-items: center; justify-content: center; gap: 10px;
    color: var(--green);
    font-weight: 400;
    font-size: 44px;
    letter-spacing: -0.5px;
  }
  .brand-dot { width: 14px; height: 14px; border-radius: 50%; background: var(--green); flex: none; }

  .identity {
    position: absolute; right: 36px; top: 158px;
    text-align: right; color: var(--white);
  }
  .identity-name { font-weight: 700; font-size: 26px; line-height: 1.1; }
  .identity-role { font-weight: 400; font-size: 18px; line-height: 1.25; }

  .contacts {
    position: absolute; right: 36px; top: 244px;
    list-style: none; color: var(--white);
    font-size: 17.5px; line-height: 22.5px; text-align: right;
  }
  .contacts li { display: flex; justify-content: flex-end; align-items: center; gap: 10px; }
  .contacts svg { width: 18px; height: 18px; flex: none; }

  .license {
    position: absolute; right: 36px; top: 328px;
    color: var(--white); font-size: 18px;
  }

  .specialties {
    position: absolute; top: 34px; left: 0; right: 0;
    text-align: center; color: var(--white);
    font-weight: 300; font-size: 18px; line-height: 22px;
  }
  .appointment {
    position: absolute; left: 51px; top: 95px;
    width: 557px; height: 267px;
    background: var(--white); border-radius: 26px;
    color: var(--green); text-align: center;
  }
  .appointment-title { font-weight: 500; font-size: 26px; margin-top: 8px; }
  .weekdays {
    display: flex; justify-content: space-between;
    padding: 0 24px; margin-top: 18px;
    font-weight: 500; font-size: 18px;
  }
  .field {
    display: flex; align-items: flex-end;
    margin-left: 62px; width: 434px;
    font-weight: 500; font-size: 20px;
  }
  .field--date { margin-top: 22px; }
  .field--time { margin-top: 14px; }
  .field-line { flex: 1; border-bottom: 2px solid var(--green); margin-left: 6px; margin-bottom: 4px; }
  .notice { margin-top: 24px; font-weight: 300; font-size: 15px; line-height: 19px; }
  .address { margin-top: 18px; font-weight: 700; font-size: 15px; }
</style>
</head>
<body>

<section class="card card--front">
  <svg class="front-shape" viewBox="0 0 660 374" preserveAspectRatio="none">
    <path d="M0 0 L234 0 C318 100 344 262 248 374 L0 374 Z" fill="var(--green)"/>
    <path d="M0 0 L212 0 C296 96 322 258 234 374 L0 374 Z" fill="var(--white)"/>
    <path d="M0 0 L208 0 C290 96 316 256 230 374 L0 374 Z" fill="var(--white)"/>
  </svg>

  <div class="brand"><span class="brand-dot"></span><span>Ferncliff</span></div>

  <div class="identity">
    <div class="identity-name">Mirela Dawkant</div>
    <div class="identity-role">Massage Therapist</div>
  </div>

  <ul class="contacts">
    <li>417-283-9061
      <svg viewBox="0 0 18 18"><path d="M2 7c0-3 14-3 14 0v1h-4V6.5H6V8H2z M4 9h10l2 6H2z" fill="var(--white)"/><circle cx="9" cy="12" r="2" fill="var(--brown)"/></svg>
    </li>
    <li>Mirela.Dawkant@mailbox.example
      <svg viewBox="0 0 18 18"><rect x="1" y="4" width="16" height="11" fill="var(--white)"/><path d="M1 4 L9 11 L17 4 M1 15 L7 9.5 M17 15 L11 9.5" stroke="var(--brown)" stroke-width="1.3" fill="none"/></svg>
    </li>
    <li>FerncliffMassage.example
      <svg viewBox="0 0 18 18" fill="none" stroke="var(--white)" stroke-width="1.3"><circle cx="9" cy="9" r="7.5"/><ellipse cx="9" cy="9" rx="3.5" ry="7.5"/><path d="M1.5 9h15M3 5h12M3 13h12M9 1.5v15"/></svg>
    </li>
  </ul>

  <div class="license">LMT# 5186</div>
</section>

<section class="card card--back">
  <p class="specialties">Science Geek, Massage Therapist, Neuromuscular Therapy<br>Cannabis Spa Treatments, Raindrop Therapy, Essential Oils</p>

  <div class="appointment">
    <h2 class="appointment-title">Appointment</h2>
    <div class="weekdays"><span>MON</span><span>TUES</span><span>WEDS</span><span>THURS</span><span>FRI</span><span>SAT</span></div>
    <div class="field field--date"><span>DATE :</span><span class="field-line"></span></div>
    <div class="field field--time"><span>TIME :</span><span class="field-line"></span></div>
    <p class="notice">This time reserved for you. If possible to keep this appointment,<br>kindly give notice one day in advance.</p>
    <p class="address">2740 NE Larkspur Ave, Kestrel Falls, OR 97000, USA</p>
  </div>
</section>

</body>
</html>
```